Tellwick Asset Management - Corporate Letter Head Project

Looking for a classy design based on our current logo. Please find current logo source file in files. With our color scheme.

Target Market(s)

We're an investment firm, the letterhead needs to look professional and attractive to clients.

Industry/Entity Type

Hedgefund

Colors
0054AA
0677BA
7BADD7
CADEEF
E8F1F8

Requirements
Must have
• Our logo, address, phone number, and email

```html
<!DOCTYPE html>
<html lang="en">
<head>
<meta charset="utf-8">
<title>Tellwick Asset Management – Letterhead</title>
<link rel="stylesheet" href="https://fonts.googleapis.com/css2?family=Lato:wght@400;700&family=Allura&display=swap">
<style>
  :root {
    --navy: #0e2a4a;
    --ink: #1f1f1f;
    --paper: #ffffff;
    --backdrop: #8a8a8a;
    --faint: #eeeeee;
  }
  * { margin: 0; padding: 0; box-sizing: border-box; }
  html, body { width: 711px; height: 1200px; overflow: hidden; }
  body { background: var(--backdrop); font-family: "Lato", sans-serif; color: var(--ink); position: relative; }

  .letterhead {
    position: absolute; left: 0; top: 97px;
    width: 711px; height: 1006px;
    background: var(--paper);
    overflow: hidden;
  }
  .masthead {
    position: absolute; left: 0; top: 0; width: 100%; height: 189px;
    background: var(--navy); color: var(--paper);
  }
  .brand {
    position: absolute; left: 40px; top: 96px; width: 220px;
    display: flex; flex-direction: column; align-items: center; gap: 8px;
  }
  .brand-mark { width: 14px; height: 14px; border: 1.5px solid var(--paper); }
  .brand-name {
    font-size: 19px; font-weight: 400; letter-spacing: 1px;
    text-transform: uppercase; text-align: center; line-height: 1.1;
  }
  .contact-list { position: absolute; left: 474px; top: 55px; list-style: none; font-size: 13px; line-height: 16px; }
  .contact-list li { display: flex; align-items: flex-start; gap: 11px; margin-bottom: 10px; }
  .contact-list li:nth-child(3) { margin-bottom: 9px; }
  .contact-list svg { width: 12px; height: 12px; flex: none; margin-top: 2px; fill: var(--paper); }

  .letter { position: absolute; left: 58px; top: 290px; width: 589px; font-size: 12.9px; line-height: 15.8px; }
  .recipient strong, .sender strong { font-weight: 700; display: block; }
  .body-copy { margin-top: 36px; }
  .body-copy p { text-align: justify; margin-bottom: 15.8px; hyphens: manual; }
  .sender { position: absolute; left: 58px; top: 736px; font-size: 12.9px; line-height: 15.8px; }
  .signature-script { font-family: "Allura", cursive; font-size: 42px; line-height: 1; margin-top: 14px; color: #111; }
  .signature-label { margin-top: 8px; }

  .decoration {
    position: absolute; left: 492px; top: 600px; width: 219px; height: 406px;
    background: radial-gradient(ellipse at 50% 50%, var(--faint) 0%, rgba(238,238,238,0) 70%);
  }
  .footer-rule { position: absolute; left: 53px; top: 959px; width: 604px; height: 1.5px; background: var(--navy); }
</style>
</head>
<body>
  <article class="letterhead">
    <header class="masthead">
      <div class="brand">
        <span class="brand-mark"></span>
        <span class="brand-name">Tellwick Asset Management</span>
      </div>
      <ul class="contact-list">
        <li>
          <svg viewBox="0 0 12 12" aria-hidden="true"><path d="M6 0a4 4 0 0 0-4 4c0 3 4 8 4 8s4-5 4-8a4 4 0 0 0-4-4zm0 5.6a1.6 1.6 0 1 1 0-3.2 1.6 1.6 0 0 1 0 3.2z"/></svg>
          <span>123, Your Company Address<br>City Name, Country 123 456</span>
        </li>
        <li>
          <svg viewBox="0 0 12 12" aria-hidden="true"><path d="M3 .5 5 3 4 4.5c.6 1.4 1.7 2.6 3.2 3.3L8.6 6.8 11 8.7 10 11C5 11 1 6.5 1 1.6z"/></svg>
          <span>0123 456 789</span>
        </li>
        <li>
          <svg viewBox="0 0 12 12" aria-hidden="true"><path d="M1 2.5h10v7H1zM1.5 3 6 6.5 10.5 3" stroke="#0e2a4a" stroke-width=".8"/></svg>
          <span>info@yourmailiid.com</span>
        </li>
        <li>
          <svg viewBox="0 0 12 12" aria-hidden="true" style="fill:none;stroke:#fff;stroke-width:.9"><circle cx="6" cy="6" r="5"/><ellipse cx="6" cy="6" rx="2.2" ry="5"/><path d="M1 6h10M2 3.5h8M2 8.5h8"/></svg>
          <span>www.yourwebsite.com</span>
        </li>
      </ul>
    </header>

    <div class="decoration" role="img" aria-label="Faint decorative network pattern"></div>

    <section class="letter">
      <div class="recipient">
        To,
        <strong>CLIENT NAME</strong>
        123, Your address goes here<br>
        Country 123456
      </div>
      <div class="body-copy">
        <p>It is a long established fact that a reader will be distracted by the readable content of a page when looking at its layout. The point of using Lorem Ipsum is that it has a more-or-less normal distribution of letters, as opposed to using 'Content here, content here', making it look like readable English. Many desktop publishing packages and web page editors now use Lorem Ipsum as their default model text, and a search for 'lorem ipsum' will uncover many web sites still in their infancy. Various versions have evolved over the years, sometimes by accident, sometimes on purpose (injected humour and the like). It is a long established fact that a reader will be distracted by the readable content of a page when looking at its layout. The point of using Lorem Ipsum is that it has a more-or-less normal distribution of letters, as opposed to using 'Content here, content here', making it look like readable English.</p>
        <p>It is a long established fact that a reader will be distracted by the readable content of a page when look&shy;ing at its layout. The point of using Lorem Ipsum is that it has a more-or-less normal distribution of let&shy;ters, as opposed to using 'Content here, content here', making it look like readable English. Many desk&shy;top publishing packages and web page editors now use Lorem Ipsum as their default model text, and a search for 'lorem ipsum' will uncover many web sites still in their infancy.</p>
        <p>Many desktop publishing packages and web page editors now use Lorem Ipsum as their default model text, and a search for 'lorem ipsum' will uncover many web sites still in their infancy.</p>
      </div>
    </section>

    <footer class="sender">
      From,
      <strong>NAME HERE</strong>
      Designation goes here
      <div class="signature-script">Signature</div>
      <div class="signature-label">Signature</div>
    </footer>

    <div class="footer-rule"></div>
  </article>
</body>
</html>
```